VMR business card

Need a business card for a company that provides instructional design and elearning development services. The website is here: http://vantmoro.studio/

I'm attaching a current logo, as well as the old business card design. While I like to keep it clean, the old design is too simplistic for my liking. The only idea I want to reuse from the old design is placing industry jargon on the back of the card, just need a better way to present it. But if you have other ideas for the back--feel free to experiment.

Please use the colors complementary to the color we have on the website. Thank you!

```html
<!DOCTYPE html>
<html lang="en">
<head>
<meta charset="utf-8">
<title>VMR business card</title>
<link rel="stylesheet" href="https://fonts.googleapis.com/css2?family=Montserrat:wght@700;800&family=Raleway:wght@300;400;700&display=swap">
<style>
  :root {
    --page: #e7e6e8;
    --card-dark-top: #221f2a;
    --card-dark-bottom: #4b4749;
    --jargon: #a8a5a7;
    --headline: #ffffff;
    --white: #ffffff;
    --accent: #d9a285;
    --brand: #2a9f98;
    --contact: #f4f2f4;
  }
  * { box-sizing: border-box; margin: 0; padding: 0; }
  html, body { width: 1200px; height: 800px; overflow: hidden; }
  body { background: var(--page); position: relative; }

  .card {
    position: absolute;
    width: 525px;
    height: 300px;
    top: 250px;
    overflow: hidden;
    box-shadow: 0 6px 18px rgba(0,0,0,0.18);
  }

  /* Back of card: service keywords around a call to action */
  .card-back {
    left: 50px;
    background: linear-gradient(180deg, var(--card-dark-top) 0%, var(--card-dark-top) 35%, var(--card-dark-bottom) 100%);
    padding: 24px 30px 0 30px;
    font-family: "Montserrat", sans-serif;
    font-weight: 800;
    text-transform: uppercase;
  }
  .keyword-line {
    font-size: 25px;
    line-height: 36px;
    color: var(--jargon);
    letter-spacing: 0.4px;
    white-space: nowrap;
  }
  .call-to-action {
    display: flex;
    align-items: center;
    gap: 12px;
    margin: 2px 0 4px;
  }
  .call-to-action-mark {
    width: 12px;
    height: 12px;
    background: var(--accent);
    flex: none;
  }
  .call-to-action-text {
    font-size: 29px;
    line-height: 38px;
    color: var(--headline);
    white-space: nowrap;
  }

  /* Front of card: identity */
  .card-front {
    right: 50px;
    background: linear-gradient(160deg, var(--card-dark-top) 0%, var(--card-dark-top) 50%, var(--card-dark-bottom) 100%);
  }
  .brand-band {
    height: 112px;
    background: var(--white);
    display: flex;
    align-items: center;
    padding-left: 34px;
    gap: 10px;
  }
  .brand-mark {
    width: 22px;
    height: 22px;
    border-radius: 50%;
    background: var(--brand);
  }
  .brand-name {
    font-family: "Raleway", sans-serif;
    font-weight: 700;
    font-size: 26px;
    color: var(--brand);
    letter-spacing: 0.3px;
  }
  .contact-block {
    position: absolute;
    right: 30px;
    top: 128px;
    text-align: right;
    font-family: "Raleway", sans-serif;
    color: var(--contact);
  }
  .person-name {
    font-size: 33px;
    line-height: 40px;
    color: var(--accent);
    margin-bottom: 12px;
  }
  .person-name .first { font-family: "Montserrat", sans-serif; font-weight: 700; }
  .person-name .last { font-weight: 300; }
  .contact-line {
    font-size: 18px;
    line-height: 27px;
    font-weight: 400;
    letter-spacing: 0.3px;
  }
</style>
</head>
<body>
  <section class="card card-back" aria-label="Card back">
    <p class="keyword-line">Storyboards Microlearning</p>
    <p class="keyword-line">Needs Analysis Authoring</p>
    <p class="keyword-line">Assessment Video UX</p>
    <div class="call-to-action">
      <span class="call-to-action-mark"></span>
      <p class="call-to-action-text">Let's build it together</p>
    </div>
    <p class="keyword-line">Onboarding Simulations</p>
    <p class="keyword-line">Accessibility Analytics</p>
    <p class="keyword-line">Virtual Training LXP</p>
  </section>

  <section class="card card-front" aria-label="Card front">
    <div class="brand-band">
      <span class="brand-mark"></span>
      <span class="brand-name">Vantmoro Studio</span>
    </div>
    <div class="contact-block">
      <p class="person-name"><span class="first">Adrian</span> <span class="last">Kessel</span></p>
      <p class="contact-line">555 014 2387</p>
      <p class="contact-line">akessel@vantmoro.studio</p>
      <p class="contact-line">www.vantmoro.studio</p>
    </div>
  </section>
</body>
</html>
```